A Clear Three Step Roadmap For Contractors

We are looking for a one-pager "roadmap" that is similar to the 2nd picture we attached, but much more professional & better... please make it landscape orientation. The logo for this system is attached below, as well.

Our Brand Colors to use:
#f2d582
#303030
#8b8c90

The copy we'd like to use on the flyer:
A Clear Three Step Roadmap that will finally allow you to attract quality customers and win more jobs.

The Keystone Ladder Method is a simple to follow system that was created specifically for Contractors and Blue Collar Business Owners.

When it comes to marketing and growing their business, the majority of Contractors are left confused, frustrated and extremely overwhelmed. Unlike most sales, marketing & training programs that offer a single "piece of the puzzle", we've mapped out each essential step of the puzzle and cut out all of the fluff.

All you have to do is complete each step in the right order and we'll be guiding you along the entire journey!

A ---> B

Blueprint: Get clear on where you're going, define your ideal audience, and finally, master your message.
Step 1: Clarify The Chaos
Step 2: Define Your Customer
Step 3: Master Your Message

Build: Attract quality leads, Build your funnel and Formulate a high-converting follow-up system
Step 4: Develop Lead Generator
Step 5: Construct Your Funnel
Step 6: Formulate the Follow-Up

Breakthrough: Get in front of your ideal customers and rapidly scale your business by driving traffic and becoming the authority in your market
Step 7: Turn-On the Traffic
Step 8: Become the Authority
Step 9: Unlock Your Growth

```html
<!DOCTYPE html>
<html lang="en">
<head>
<meta charset="utf-8">
<title>Keystone Ladder Method – Three Step Roadmap</title>
<link href="https://fonts.googleapis.com/css2?family=Lato:ital,wght@0,400;0,700;0,900;1,900&display=swap" rel="stylesheet">
<style>
  :root {
    --gold: #f2d582;
    --gold-band: #ecd17f;
    --gold-pill: #f4e2a6;
    --ink: #303030;
    --steel: #8b8c90;
    --paper: #ffffff;
    --road: #232323;
    --mist: #e4e5e7;
  }
  * { box-sizing: border-box; margin: 0; padding: 0; }
  html, body { width: 1200px; height: 709px; overflow: hidden; }
  body {
    position: relative;
    font-family: "Lato", sans-serif;
    color: var(--ink);
    background: linear-gradient(180deg, var(--paper) 0%, var(--paper) 55%, var(--mist) 100%);
  }
  .header {
    position: absolute; left: 0; top: 0; width: 1200px; height: 145px;
    background: var(--gold-band);
  }
  .brand {
    position: absolute; left: 55px; top: 24px; width: 385px; height: 108px;
    background: var(--paper); border: 4px solid var(--ink); border-radius: 6px;
    display: flex; align-items: center; gap: 16px; padding-left: 22px;
  }
  .brand-mark { width: 44px; height: 44px; background: var(--gold); flex: none; }
  .brand-name {
    font-weight: 900; font-size: 33px; line-height: 1.02; color: var(--ink);
    text-transform: uppercase; letter-spacing: 0.5px;
  }
  .tagline {
    position: absolute; left: 470px; top: 40px; width: 700px;
    text-align: center; font-style: italic; font-weight: 900; font-size: 26px; line-height: 1.28;
    color: var(--ink);
  }
  .intro {
    position: absolute; left: 74px; top: 160px; width: 1060px;
    font-weight: 700; font-size: 14px; line-height: 1.35;
  }
  .intro p { margin-bottom: 14px; }
  .intro .closing { width: 470px; }
  .road {
    position: absolute; left: 0; top: 411px; width: 1200px; height: 205px;
    background: var(--road);
  }
  .lane {
    position: absolute; left: 0; width: 1200px; height: 3px;
    background: repeating-linear-gradient(90deg, var(--paper) 0 70px, transparent 70px 120px);
  }
  .lane-a { top: 475px; }
  .lane-b { top: 555px; }
  .step {
    position: absolute; left: 53px; width: 442px; height: 112px;
    background: var(--gold-pill); border-radius: 0 56px 56px 0;
    display: flex; align-items: center; padding-left: 24px; gap: 22px;
  }
  .step-1 { top: 312px; }
  .step-2 { top: 438px; }
  .step-3 { top: 565px; }
  .step-num {
    width: 72px; height: 72px; flex: none; border-radius: 50%;
    border: 3px solid var(--ink); box-shadow: inset 0 0 0 4px var(--gold), inset 0 0 0 6px var(--ink);
    background: var(--paper);
    display: flex; align-items: center; justify-content: center;
    font-weight: 900; font-size: 42px;
  }
  .step-title { font-weight: 900; font-size: 34px; line-height: 1; text-transform: uppercase; }
  .step-text { font-weight: 700; font-size: 10px; line-height: 1.35; margin-top: 6px; width: 320px; }
  .screen-card {
    position: absolute; left: 560px; top: 258px; width: 590px; height: 416px;
    background: var(--paper); border: 2px solid #e8dcb0; border-radius: 26px;
    box-shadow: 0 4px 14px rgba(0,0,0,0.18);
  }
  .roadmap {
    position: absolute; left: 615px; top: 278px; width: 476px; height: 375px;
  }
  .roadmap text { font-family: "Lato", sans-serif; }
  .node-label { font-size: 7px; font-weight: 700; fill: var(--gold); text-anchor: middle; }
  .row-label { font-size: 10px; font-weight: 900; fill: var(--paper); }
</style>
</head>
<body>
  <header class="header">
    <div class="brand">
      <span class="brand-mark"></span>
      <span class="brand-name">Keystone<br>Ladder Method</span>
    </div>
    <h1 class="tagline">A Clear Three Step Roadmap that will finally allow you to attract quality customers and win more jobs.</h1>
  </header>

  <section class="intro">
    <p>The Keystone Ladder Method is a simple to follow system that was created specifically for Contractors and Blue Collar Business Owners</p>
    <p>When it comes to growing their business, the majority of Contractors are left confused, frustrated and extremely overwhelmed. Unlike most sales, marketing &amp; training programs that offer a single "piece of the puzzle", we've mapped out each essential step of the puzzle and cut out all of the fluff.</p>
    <p class="closing">All you have to do is complete each step in the right order and we'll be guiding you along the entire journey!</p>
  </section>

  <div class="road"></div>
  <div class="lane lane-a"></div>
  <div class="lane lane-b"></div>

  <div class="step step-1">
    <div class="step-num">1</div>
    <div><div class="step-title">Blueprint</div><p class="step-text">Get clear on where you're going, define your ideal audience, and finally master your message</p></div>
  </div>
  <div class="step step-2">
    <div class="step-num">2</div>
    <div><div class="step-title">Build</div><p class="step-text">Attract quality leads, Build your funnel and Formulate a high-converting follow-up system</p></div>
  </div>
  <div class="step step-3">
    <div class="step-num">3</div>
    <div><div class="step-title">Breakthrough</div><p class="step-text">Get in front of your ideal customers and rapidly scale your business by driving traffic and becoming the authority in your market</p></div>
  </div>

  <div class="screen-card"></div>
  <svg class="roadmap" viewBox="0 0 476 375" role="img" aria-label="Nine step roadmap from A to B">
    <defs>
      <linearGradient id="slate" x1="0" y1="0" x2="1" y2="1">
        <stop offset="0" stop-color="#3a3a3a"/><stop offset="1" stop-color="#1c1c1c"/>
      </linearGradient>
    </defs>
    <rect width="476" height="375" fill="url(#slate)"/>
    <g stroke="#bdbdbd" stroke-width="1" stroke-dasharray="4 3" fill="none">
      <line x1="154" y1="94" x2="407" y2="94"/>
      <line x1="154" y1="183" x2="407" y2="183"/>
      <line x1="154" y1="277" x2="407" y2="277"/>
      <line x1="407" y1="183" x2="407" y2="277"/>
      <line x1="154" y1="94" x2="154" y2="183"/>
    </g>
    <g stroke="#bdbdbd" stroke-width="1" fill="none">
      <line x1="140" y1="300" x2="120" y2="330"/>
      <line x1="430" y1="84" x2="455" y2="70"/>
    </g>
    <text x="112" y="345" font-size="16" font-weight="900" fill="var(--gold)">A</text>
    <text x="456" y="70" font-size="16" font-weight="900" fill="var(--gold)">B</text>

    <g fill="var(--paper)" stroke="var(--steel)" stroke-width="2">
      <circle cx="154" cy="94" r="26"/><circle cx="281" cy="94" r="26"/><circle cx="407" cy="94" r="26"/>
      <circle cx="154" cy="183" r="26"/><circle cx="281" cy="183" r="26"/><circle cx="407" cy="183" r="26"/>
      <circle cx="154" cy="277" r="26"/><circle cx="281" cy="277" r="26"/><circle cx="407" cy="277" r="26"/>
    </g>
    <g fill="var(--gold)">
      <circle cx="154" cy="94" r="10"/><circle cx="281" cy="94" r="10"/><circle cx="407" cy="94" r="10"/>
      <circle cx="154" cy="183" r="10"/><circle cx="281" cy="183" r="10"/><circle cx="407" cy="183" r="10"/>
      <circle cx="154" cy="277" r="10"/><circle cx="281" cy="277" r="10"/><circle cx="407" cy="277" r="10"/>
    </g>

    <text class="node-label" x="154" y="62">Turn-On the Traffic</text>
    <text class="node-label" x="281" y="62">Become the Authority</text>
    <text class="node-label" x="407" y="62">Unlock Your Growth</text>
    <text class="node-label" x="154" y="150">Formulate the Follow-Up</text>
    <text class="node-label" x="281" y="150">Construct Your Funnel</text>
    <text class="node-label" x="407" y="150">Develop Lead Generator</text>
    <text class="node-label" x="154" y="245">Clarify the Chaos</text>
    <text class="node-label" x="281" y="245">Define Your Customer</text>
    <text class="node-label" x="407" y="245">Master Your Message</text>

    <g fill="var(--paper)" stroke="var(--gold)" stroke-width="1">
      <rect x="8" y="88" width="14" height="16" rx="2"/>
      <rect x="8" y="176" width="14" height="16" rx="2"/>
      <rect x="8" y="271" width="14" height="16" rx="2"/>
    </g>
    <g font-size="10" font-weight="700" fill="var(--ink)" text-anchor="middle">
      <text x="15" y="100">3</text><text x="15" y="188">2</text><text x="15" y="283">1</text>
    </g>
    <text class="row-label" x="31" y="100">BREAKTHROUGH</text>
    <text class="row-label" x="31" y="188">BUILD</text>
    <text class="row-label" x="31" y="283">BLUEPRINT</text>
    <g stroke="var(--gold)" stroke-width="1.5">
      <line x1="31" y1="104" x2="118" y2="104"/>
      <line x1="31" y1="192" x2="76" y2="192"/>
      <line x1="31" y1="287" x2="94" y2="287"/>
    </g>
    <text x="466" y="366" font-size="9" fill="var(--paper)" text-anchor="end">Keystone Ladder Method ©</text>
  </svg>
</body>
</html>
```